Brass Kettle Business Card

I needed some business cards done for my band. We are a 9 piece funk/horn band that plays a lot of private parties, wedding receptions and music festivals. We'd like a design with vivid colors that incorporates our logo. You can check out our website at www.brasskettleband.com to see what type of vibe we are going for.

```html
<!DOCTYPE html>
<html lang="en">
<head>
<meta charset="UTF-8">
<title>Brass Kettle Business Card</title>
<link href="https://fonts.googleapis.com/css2?family=Open+Sans:wght@400;700;800&display=swap" rel="stylesheet">
<style>
  :root {
    --backdrop: #2e2e2e;
    --card: #1a1a1a;
    --card-edge: #111111;
    --lime: #c9da2f;
    --wave-grey: #3d3d3d;
    --text-light: #e8e8e8;
  }
  * { box-sizing: border-box; margin: 0; padding: 0; }
  html, body {
    width: 1200px; height: 689px; overflow: hidden;
    background: var(--backdrop);
    font-family: "Open Sans", Arial, sans-serif;
  }
  .stage {
    position: relative; width: 1200px; height: 689px;
  }
  .card {
    position: absolute; top: 190px;
    width: 520px; height: 300px;
    background: var(--card);
    border-radius: 22px;
    overflow: hidden;
    box-shadow: 0 14px 30px rgba(0,0,0,.45);
  }
  .card--front { left: 45px; }
  .card--back { left: 635px; }

  .front-name {
    position: absolute; inset: 0;
    display: flex; align-items: center; justify-content: center;
    color: var(--lime);
    font-weight: 800; font-size: 62px; letter-spacing: -1px;
  }

  .brand-mark {
    position: absolute; left: 40px; top: 62px;
    width: 170px; height: 170px;
    border-radius: 50%;
    border: 14px solid var(--lime);
    background: #0d0d0d;
    display: flex; align-items: center; justify-content: center;
    text-align: center;
  }
  .brand-mark__name {
    color: var(--lime);
    font-weight: 800; font-size: 22px; line-height: 1.1;
  }

  .divider {
    position: absolute; left: 250px; top: 50px;
    width: 2px; height: 150px;
    background: var(--lime);
  }

  .contact {
    position: absolute; left: 272px; top: 44px;
    color: var(--text-light);
    font-size: 13px; line-height: 1.45;
  }
  .contact__name {
    color: var(--lime); font-weight: 700; font-size: 22px; line-height: 1.1;
  }
  .contact__role { font-size: 13px; margin-bottom: 12px; }
  .contact__row { display: flex; align-items: center; gap: 7px; }
  .contact__row svg { width: 11px; height: 11px; fill: var(--lime); flex: none; }
  .contact__address { margin-top: 12px; }

  .wave { position: absolute; left: 0; bottom: 0; width: 520px; height: 120px; }
</style>
</head>
<body>
<main class="stage">

  <section class="card card--front" aria-label="Card front">
    <div class="front-name">Brass Kettle</div>
  </section>

  <section class="card card--back" aria-label="Card back">
    <div class="brand-mark">
      <span class="brand-mark__name">Brass<br>Kettle</span>
    </div>

    <div class="divider"></div>

    <div class="contact">
      <p class="contact__name">Dale Corwin</p>
      <p class="contact__role">Managing Director</p>
      <p class="contact__row">
        <svg viewBox="0 0 24 24" aria-hidden="true"><path d="M6.6 10.8a15.1 15.1 0 0 0 6.6 6.6l2.2-2.2a1 1 0 0 1 1-.25 11.4 11.4 0 0 0 3.6.57 1 1 0 0 1 1 1V20a1 1 0 0 1-1 1A17 17 0 0 1 3 4a1 1 0 0 1 1-1h3.5a1 1 0 0 1 1 1c0 1.25.2 2.45.57 3.57a1 1 0 0 1-.25 1z"/></svg>
        555.210.7734
      </p>
      <p class="contact__row">
        <svg viewBox="0 0 24 24" aria-hidden="true"><path d="M2 5h20v14H2zm2 2v.5l8 5 8-5V7z"/></svg>
        info@brasskettleband.com
      </p>
      <p class="contact__row">
        <svg viewBox="0 0 24 24" aria-hidden="true"><circle cx="12" cy="12" r="10"/></svg>
        www.brasskettleband.com
      </p>
      <p class="contact__address">Your address, City<br>State, Zip 1234</p>
    </div>

    <svg class="wave" viewBox="0 0 520 120" preserveAspectRatio="none" aria-hidden="true">
      <path d="M0 70 C150 115 330 95 520 18 L520 120 L0 120 Z" fill="var(--wave-grey)"/>
      <path d="M0 92 C160 128 340 108 520 38 L520 120 L0 120 Z" fill="var(--lime)"/>
      <path d="M0 108 C170 135 350 118 520 70 L520 120 L0 120 Z" fill="var(--card)"/>
    </svg>
  </section>

</main>
</body>
</html>
```